Meridian Sound Wellness LLC Card Design

Need business card with a logo for a hearing aid sales and audiology business. We have two Hearing Instrument Specialists and one Audiologist on staff. Over 25 years in business. Locally owned and operated. Financing available. Most insurances accepted.

Meridian Sound Wellness LLC
48730 W Linden Row, Suite 9
Spokane, WA 99481
509-617-2085
www.meridiansoundnorth.example

Manager
Tobias Wrenfield HIS COHC
License #81729046

Target Market(s)

50yr old + people with a hearing loss.

Industry/Entity Type

Business

Contact Information for Business Card

48730 W Linden Row, Suite 9
Spokane, WA 99481
509-617-2085
www.meridiansoundnorth.example

Manager
Tobias Wrenfield HIS COHC
NRPL #81729046

Font styles to use
Serif
Sans Serif

Requirements
Must have
• Business name, Tobias's name and title(s) and contact information, License #, web address
Nice to have
Should not have

```html
<!DOCTYPE html>
<html lang="en">
<head>
<meta charset="utf-8">
<title>Meridian Sound Wellness LLC – Business Card</title>
<link rel="stylesheet" href="https://fonts.googleapis.com/css2?family=Open+Sans:wght@400;600;700&display=swap">
<style>
  :root {
    --stage: #000000;
    --card-front: #0f68a3;
    --card-back: #206509;
    --ink: #ffffff;
    --ink-soft: rgba(255, 255, 255, 0.14);
  }
  * { margin: 0; padding: 0; box-sizing: border-box; }
  html, body {
    width: 1200px; height: 900px; overflow: hidden;
    background: var(--stage);
    font-family: "Open Sans", Arial, sans-serif;
    color: var(--ink);
  }
  .canvas { position: relative; width: 1200px; height: 900px; }

  .card { position: absolute; top: 275px; width: 477px; height: 293px; }
  .card--front {
    left: 116px; background: var(--card-front);
    border-radius: 0 62px 0 62px;
  }
  .card--back {
    left: 622px; background: var(--card-back);
    border-radius: 62px 0 62px 0;
  }

  .brand-shape {
    position: absolute; left: 74px; top: 42px;
    width: 164px; height: 62px; background: var(--ink-soft);
  }
  .brand-name--front {
    position: absolute; left: 39px; top: 104px;
    font-size: 21px; font-weight: 600; line-height: 1.2;
  }

  .holder { position: absolute; right: 32px; top: 38px; text-align: right; }
  .holder__name { font-size: 15px; font-weight: 700; }
  .holder__creds { font-size: 12px; font-weight: 600; }
  .holder__title { font-size: 12px; font-weight: 400; margin-top: 1px; }

  .license {
    position: absolute; right: 32px; top: 176px;
    font-size: 13px; font-weight: 700;
  }
  .contact {
    position: absolute; right: 28px; top: 207px;
    list-style: none; text-align: right; font-size: 13px;
  }
  .contact li { display: flex; justify-content: flex-end; align-items: center; gap: 6px; height: 17px; }
  .contact svg { width: 11px; height: 11px; }
  .address {
    position: absolute; right: 32px; top: 255px;
    font-size: 13px; font-style: normal;
  }

  .brand-lockup {
    position: absolute; inset: 0;
    display: flex; align-items: center; justify-content: center; gap: 16px;
  }
  .brand-lockup__dot { width: 22px; height: 22px; border-radius: 50%; background: var(--ink); }
  .brand-name--back { font-size: 30px; font-weight: 600; line-height: 1.2; }
</style>
</head>
<body>
<main class="canvas">
  <section class="card card--front" aria-label="Card front">
    <div class="brand-shape" aria-hidden="true"></div>
    <p class="brand-name--front">Meridian Sound Wellness LLC</p>

    <div class="holder">
      <p><span class="holder__name">Tobias Wrenfield</span> <span class="holder__creds">HIS COHC</span></p>
      <p class="holder__title">Manager</p>
    </div>

    <p class="license">License #81729046</p>

    <ul class="contact">
      <li>509-617-2085
        <svg viewBox="0 0 24 24" aria-hidden="true"><path fill="#fff" d="M6.6 10.8a15.1 15.1 0 0 0 6.6 6.6l2.2-2.2c.3-.3.7-.4 1-.2 1.1.4 2.3.6 3.6.6.6 0 1 .4 1 1V20c0 .6-.4 1-1 1A17 17 0 0 1 3 4c0-.6.4-1 1-1h3.5c.6 0 1 .4 1 1 0 1.3.2 2.5.6 3.6.1.3 0 .7-.2 1z"/></svg>
      </li>
      <li>www.meridiansoundnorth.example
        <svg viewBox="0 0 24 24" aria-hidden="true"><circle cx="12" cy="12" r="10" fill="#fff"/><path d="M2 12h20M12 2c3 3 3 17 0 20M12 2c-3 3-3 17 0 20" stroke="#0f68a3" stroke-width="1.6" fill="none"/></svg>
      </li>
    </ul>

    <address class="address">48730 W Linden Row, Suite 9, Spokane, WA 99481</address>
  </section>

  <section class="card card--back" aria-label="Card back">
    <div class="brand-lockup">
      <span class="brand-lockup__dot" aria-hidden="true"></span>
      <p class="brand-name--back">Meridian Sound<br>Wellness LLC</p>
    </div>
  </section>
</main>
</body>
</html>
```